city centre based IT support firm flyer.

We need a flyer to boost our business. We're a tech support firm based in city centre, London and provide helpdesk and call out support to SMEs in and around London.
They'll be two flyers with the same design. One is location specific and has the copy:
-
1 Month Free IT Support!
Based in city centre, we provide expert tech support for both laptops and PCs.
We have monthly as well as pay-as-you-go plans to fit your business.
Call us now and we'll show you how we can save you up to 50% on your IT spend.
-None location based is-
1 Month Free IT Support!
We provide expert, professional tech support for both laptops and PCs.
• Dedicated full time helpdesk
• Same day onsite visits
• Proactive support with monitoring
• 98% satisfaction score*
*taken from satisfaction survey sent out on closure of every case for Oct 2011 to Oct 2012
-
The location one needs to include a map with our location marked as postcode W9K 4TP.
I'm fine with royalty photos being used within a reasonable price. Please use PixQuarry.
Our site shows our brand best. Please keep as close to this as possible.
http://brisk-byte.example
Thanks for looking.

```html
<!DOCTYPE html>
<html lang="en">
<head>
<meta charset="utf-8">
<title>BriskByte – Friendly &amp; Reliable Tech Support</title>
<link rel="stylesheet" href="https://fonts.googleapis.com/css2?family=Cinzel:wght@500;600;700&family=Open+Sans:ital,wght@0,400;0,600;0,700;0,800;1,800&family=Mulish:wght@400&display=swap">
<style>
  :root {
    --stage: #e9e7e3;
    --paper: #ffffff;
    --lime: #c3d72f;
    --brand-green: #9bc13a;
    --orange: #f59c29;
    --ink: #1a1a1a;
    --rule: #b9b9b9;
    --photo-office-a: #c9ced3;
    --photo-office-b: #8d939a;
    --photo-agent-a: #b38a6c;
    --photo-agent-b: #e8e3df;
    --map-a: #ece8e0;
    --map-b: #d9d4c8;
  }
  * { margin: 0; padding: 0; box-sizing: border-box; }
  html, body { width: 930px; height: 1200px; overflow: hidden; }
  body { background: var(--stage); position: relative; font-family: "Open Sans", sans-serif; color: var(--ink); }

  .flyer {
    position: absolute; left: 65px; top: 33px;
    width: 800px; height: 1136px;
    background: var(--paper);
    box-shadow: 0 4px 18px rgba(0,0,0,.25);
    overflow: hidden;
  }

  .masthead { position: absolute; left: 0; top: 0; width: 800px; height: 148px; display: flex; align-items: center; justify-content: center; }
  .brand-name { font-family: "Open Sans", sans-serif; font-weight: 700; font-size: 70px; letter-spacing: -1px; color: var(--brand-green); }

  .photo-strip { position: absolute; left: 0; top: 148px; width: 800px; height: 352px; border-top: 4px solid var(--rule); border-bottom: 4px solid var(--rule); display: flex; }
  .photo { height: 100%; }
  .photo--office { width: 421px; background: linear-gradient(160deg, var(--photo-office-a), #eef0f2 45%, var(--photo-office-b)); border-right: 3px solid var(--rule); }
  .photo--agents { flex: 1; background: linear-gradient(110deg, var(--photo-agent-a), #6d5040 45%, var(--photo-agent-b)); }

  .offer-panel { position: absolute; left: 0; top: 500px; width: 800px; height: 446px; background: var(--lime); text-align: center; }
  .offer-title { position: absolute; top: 48px; width: 100%; font-family: "Cinzel", serif; font-weight: 700; font-size: 31px; letter-spacing: 2px; }
  .offer-title small { font-size: 23px; }
  .offer-tagline { position: absolute; top: 90px; width: 100%; font-family: "Cinzel", serif; font-weight: 600; font-size: 17px; letter-spacing: 3px; }

  .selling-points { position: absolute; left: 40px; top: 140px; list-style: none; text-align: left; font-weight: 800; font-size: 19px; line-height: 1.25; }
  .selling-points li { padding-left: 14px; text-indent: -14px; margin-bottom: 8px; }
  .selling-points li::before { content: "• "; }

  .free-offer { position: absolute; top: 268px; width: 100%; font-weight: 700; font-size: 31px; }
  .free-offer b { font-size: 46px; font-weight: 800; }

  .features { position: absolute; top: 332px; width: 100%; font-family: "Mulish", sans-serif; font-size: 22px; line-height: 38px; }
  .footnote { position: absolute; top: 414px; width: 100%; font-family: "Mulish", sans-serif; font-size: 15.5px; }

  .contact-band { position: absolute; left: 0; top: 946px; width: 800px; height: 190px; border-top: 8px solid var(--rule); background: var(--orange); }
  .helpdesk-label { position: absolute; left: 62px; top: 14px; font-weight: 800; font-style: italic; font-size: 30px; }
  .helpdesk-phone { position: absolute; left: 60px; top: 46px; font-weight: 800; font-size: 56px; letter-spacing: 1px; }
  .site-url { position: absolute; left: 62px; top: 130px; font-weight: 700; font-size: 24px; letter-spacing: 4px; }
  .location-map { position: absolute; right: 4px; top: 4px; width: 228px; height: 172px; background: linear-gradient(135deg, var(--map-a), var(--map-b)); }
</style>
</head>
<body>
  <main class="flyer">
    <header class="masthead">
      <span class="brand-name">BriskByte</span>
    </header>

    <section class="photo-strip">
      <div class="photo photo--office" role="img" aria-label="Stock photo of an office team working together at a laptop"></div>
      <div class="photo photo--agents" role="img" aria-label="Stock photo of two smiling helpdesk agents wearing headsets"></div>
    </section>

    <section class="offer-panel">
      <h1 class="offer-title">Friendly &amp; Reliable <small>Tech Support</small></h1>
      <p class="offer-tagline">A one stop shop for all your business IT needs</p>
      <ul class="selling-points">
        <li>Call us now and we'll show you how we can save you up to<br>50% on your IT spend.</li>
        <li>We provide expert, professional tech support for both laptops and PCs.</li>
        <li>We have monthly as well as pay-as-you-go plans to fit your business.</li>
      </ul>
      <h2 class="free-offer"><b>1</b> Month Free IT Support!</h2>
      <p class="features">• Proactive support with monitoring &nbsp;• Dedicated full time helpdesk<br>• Same day onsite visits &nbsp;• 98% satisfaction score*</p>
      <p class="footnote">*taken from satisfaction survey sent out on closure of every case for Oct 2011 to Oct 2012</p>
    </section>

    <footer class="contact-band">
      <p class="helpdesk-label">THE HELPDESK</p>
      <p class="helpdesk-phone">0203 555 0147</p>
      <p class="site-url">http://brisk-byte.example</p>
      <div class="location-map" role="img" aria-label="Street map with the office marked at postcode W9K 4TP"></div>
    </footer>
  </main>
</body>
</html>
```